Wedding Photo Studio needs custom webpage

I'm changing up my service offering to offer multiple editing styles. I'm looking to update my website to reflect that but still showcase my dreamy edits as an attention grabbing part of the website.

I will have 4 color editing styles (Colm's Hallmark, Bright & Airy, Silken Oak, Dreamy) and one black and white style. I have attached sample images in each style.

I also attached a couple dreamy edits that can be used as attention grabbing images.

I'm hoping for some functionality that perhaps takes a single image and divides it by 4 to show 25% in each style that can be clicked on and would 'maximize' the carousel to that style but still have a functionality to go to a different style after being maximized.

You can see www.colmvphotography.com for the current design and content. It doesn't have to be too different (but can be). It just needs to showcase the multiple editing styles effectively.

Target Market(s)

Couples who are having $20-50k weddings.

Industry/Entity Type

Photography

Coding

Coded - Design and coding required

Number of Pages Required

3 page

Colors

Designer to choose colors to be used in the design.

Requirements
Must have
• Pricing page with toggles for (off-season/on-season, Saturday/non-saturday) accurate pricing, good way to show multiple editing style photos.

```html
<!DOCTYPE html>
<html lang="en">
<head>
<meta charset="utf-8">
<title>Colm V Photography – Wedding Photographer</title>
<link href="https://fonts.googleapis.com/css2?family=Raleway:wght@300;400;500&family=Nunito+Sans:wght@400;600&family=Parisienne&display=swap" rel="stylesheet">
<style>
:root{
  --blue:#0a56a8;
  --ink:#2b2b2b;
  --muted:#555;
  --soft:#f3f3f3;
  --card:#232323;
  --field:#efefef;
  --white:#fff;
}
*{box-sizing:border-box;margin:0;padding:0}
html,body{width:1200px;height:5291px;overflow:hidden}
body{position:relative;background:var(--white);font-family:"Nunito Sans",sans-serif;color:var(--ink)}
.abs{position:absolute}
.heading{font-family:"Raleway",sans-serif;font-weight:300;color:var(--ink);letter-spacing:.5px;white-space:nowrap}
.kicker{font-family:"Raleway",sans-serif;font-weight:500;color:var(--blue);font-size:18px;white-space:nowrap}
.photo{position:absolute}

/* header */
.site-header{left:0;top:0;width:1200px;height:100px;background:var(--white)}
.brand{left:68px;top:22px;color:var(--blue);font-family:"Raleway",sans-serif;font-weight:400;line-height:1}
.brand .name{font-size:40px;display:block}
.brand .tag{font-size:12px;letter-spacing:2px;display:block;margin-top:4px;padding-left:30px}
.nav{left:0;top:0;width:1200px;height:100px;font-family:"Raleway",sans-serif;font-size:13px;font-weight:500;color:var(--ink)}
.nav a{position:absolute;top:50px;color:inherit;text-decoration:none}
.nav a.active{color:var(--blue);border-bottom:1px solid var(--blue);padding-bottom:3px}
.nav a.cta{top:41px;left:1011px;width:121px;height:35px;background:var(--blue);color:var(--white);text-align:center;line-height:35px;font-size:12px}

/* hero */
.hero{left:0;top:100px;width:1200px;height:773px;background:
  radial-gradient(ellipse 260px 120px at 820px 90px,rgba(255,230,150,.9),rgba(255,180,60,0) 70%),
  linear-gradient(180deg,#b9431b 0%,#e8771f 22%,#f4a032 34%,#8f8a3a 46%,#6f8a2f 62%,#4f6e22 100%)}
.hero-script{left:534px;top:510px;width:590px;font-family:"Parisienne",cursive;font-size:62px;color:var(--white);white-space:nowrap}
.hero-title{left:534px;top:598px;width:580px;text-align:center;font-family:"Raleway",sans-serif;font-weight:300;font-size:41px;color:var(--white);white-space:nowrap}
.btn-ghost{display:flex;align-items:center;justify-content:center;gap:12px;font-family:"Raleway",sans-serif;font-weight:500;letter-spacing:.5px}
.hero-btn{left:711px;top:701px;width:224px;height:72px;border:2px solid var(--white);color:var(--white);font-size:18px}
.dot{position:absolute;width:8px;height:8px;border-radius:50%}

/* styles gallery: one scene, five colour grades */
.styles-title{left:0;top:1010px;width:1200px;text-align:center;font-size:50px}
.styles-sub{left:0;top:1094px;width:1200px;text-align:center;font-size:15px;line-height:29px;color:var(--muted)}
.tile{position:absolute;overflow:hidden}
.tile .frame{position:absolute;inset:12px;border:1px solid rgba(255,255,255,.75)}
.tile .label{position:absolute;left:0;right:0;bottom:22px;text-align:center;color:var(--white);font-family:"Raleway",sans-serif;font-size:23px;text-shadow:0 1px 3px rgba(0,0,0,.35)}
.grade-dreamy{background:
  radial-gradient(ellipse 60% 45% at 55% 30%,rgba(255,170,80,.95),rgba(255,120,60,0) 70%),
  radial-gradient(ellipse 40% 35% at 50% 75%,rgba(245,235,240,.8),rgba(245,235,240,0) 70%),
  linear-gradient(180deg,#1b1d3a 0%,#5a2c4a 35%,#c0603a 60%,#3a2434 100%)}
.grade-bw{background:
  radial-gradient(ellipse 40% 45% at 62% 60%,rgba(235,235,235,.9),rgba(235,235,235,0) 70%),
  radial-gradient(ellipse 30% 50% at 30% 55%,rgba(20,20,20,.85),rgba(20,20,20,0) 70%),
  linear-gradient(160deg,#9a9a9a 0%,#4a4a4a 45%,#bdbdbd 75%,#2a2a2a 100%)}
.grade-hallmark{background:
  radial-gradient(ellipse 35% 40% at 62% 68%,rgba(240,236,228,.95),rgba(240,236,228,0) 70%),
  radial-gradient(ellipse 25% 45% at 35% 58%,rgba(40,44,58,.85),rgba(40,44,58,0) 70%),
  linear-gradient(180deg,#7e8a66 0%,#a39a86 30%,#b8a78e 55%,#6f7a5a 80%,#5a5448 100%)}
.grade-airy{background:
  radial-gradient(ellipse 40% 45% at 65% 62%,rgba(255,255,255,.95),rgba(255,255,255,0) 70%),
  radial-gradient(ellipse 25% 45% at 38% 58%,rgba(110,120,135,.6),rgba(110,120,135,0) 70%),
  linear-gradient(160deg,#e6efe0 0%,#c9dcc0 35%,#f4f6f1 65%,#d8e4cf 100%)}
.grade-oak{background:
  radial-gradient(ellipse 40% 45% at 55% 62%,rgba(232,214,196,.9),rgba(232,214,196,0) 70%),
  radial-gradient(ellipse 25% 45% at 35% 55%,rgba(38,22,16,.85),rgba(38,22,16,0) 70%),
  linear-gradient(160deg,#4a2618 0%,#8a4a2c 35%,#b06a40 60%,#5a3020 100%)}

/* about */
.about-title{left:119px;top:1832px;font-size:52px}
.line{position:absolute;height:1px;background:var(--blue)}
.about-text{left:123px;top:1977px;width:560px;font-size:12.5px;line-height:24.6px;color:var(--ink)}
.btn-outline{position:absolute;border:1.5px solid var(--blue);color:var(--ink);font-size:14px}

/* portfolio */
.portfolio-bg{left:0;top:2304px;width:1200px;height:1079px;background:var(--soft)}
.portfolio-title{left:62px;top:2432px;font-size:52px}

/* serving */
.serving{left:0;top:3383px;width:1200px;height:316px;background:var(--blue)}
.serving-frame{left:68px;top:3452px;width:1064px;height:202px;border:1.5px solid rgba(255,255,255,.85)}
.serving-title{left:400px;top:3424px;width:400px;text-align:center;background:var(--blue);color:var(--white);font-family:"Raleway",sans-serif;font-weight:400;font-size:46px}
.serving-cities{left:68px;top:3512px;width:1064px;text-align:center;color:var(--white);font-family:"Raleway",sans-serif;font-size:31px;line-height:54px}

/* testimonials */
.test-title{left:0;top:3820px;width:1200px;text-align:center;font-size:50px}
.test-kicker{left:0;top:3887px;width:1200px;text-align:center}
.quote-card{position:absolute;top:3995px;width:347px;height:263px;background:var(--card);color:var(--white);text-align:center}
.quote-card .mark{font-family:"Raleway",sans-serif;font-size:96px;font-weight:500;line-height:1;margin-top:14px;height:48px;color:#c9c9c9;overflow:hidden}
.quote-card p{font-size:11.5px;line-height:19px;padding:16px 32px 0;height:135px}
.quote-card .who{font-size:11px;letter-spacing:.5px}
.avatar{position:absolute;width:66px;height:66px;border-radius:50%;border:3px solid var(--white)}
.arrow-btn{position:absolute;width:40px;height:40px;border-radius:50%;background:#bdbdbd;display:flex;align-items:center;justify-content:center}

/* contact */
.contact-band{left:0;top:4864px;width:1200px;height:427px;background:var(--blue)}
.contact-panel{left:68px;top:4864px;width:1064px;height:163px;background:var(--white)}
.contact-title{left:542px;top:4526px;font-size:52px}
.field{position:absolute;background:var(--field);color:#6a6a6a;font-size:14px;padding:14px 0 0 28px}
.submit{position:absolute;left:553px;top:4891px;width:513px;height:47px;background:var(--blue);color:var(--white);text-align:center;line-height:47px;font-family:"Raleway",sans-serif;font-size:15px;font-weight:500}

/* footer */
.footer-brand{left:60px;top:5070px;color:var(--white);font-family:"Raleway",sans-serif;font-weight:400;line-height:1}
.footer-brand .name{font-size:56px;display:block}
.footer-brand .tag{font-size:17px;letter-spacing:2px;display:block;margin-top:6px;padding-left:80px}
.info-icon{position:absolute;width:62px;height:62px;border-radius:50%;border:2px solid var(--white);display:flex;align-items:center;justify-content:center}
.info{position:absolute;color:var(--white);font-family:"Raleway",sans-serif;font-size:17px;line-height:26px;white-space:nowrap}
.rule{left:68px;top:5213px;width:1064px;height:1px;background:rgba(255,255,255,.7)}
.copy{left:99px;top:5224px;color:var(--white);font-size:11px}
.social{position:absolute;top:5232px;width:24px;height:24px;border:1.5px solid var(--white)}
.foot-links{left:713px;top:5233px;color:var(--white);font-family:"Raleway",sans-serif;font-size:12px;white-space:nowrap}
</style>
</head>
<body>

<header class="abs site-header">
  <div class="abs brand"><span class="name">Colm V</span><span class="tag">PHOTOGRAPHY</span></div>
  <nav class="abs nav">
    <a class="active" style="left:511px">HOME</a>
    <a style="left:600px">THE TEAM</a>
    <a style="left:717px">PORTFOLIO</a>
    <a style="left:843px">BLOG</a>
    <a style="left:930px">PRICING</a>
    <a class="cta">CONTACT ME</a>
  </nav>
</header>

<section class="abs hero" role="img" aria-label="Bride and groom standing in a green field at sunset"></section>
<div class="abs hero-script">Kitchener &nbsp;– Waterloo</div>
<div class="abs hero-title">WEDDING PHOTOGRAPHER</div>
<div class="abs hero-btn btn-ghost">CONTACT US
  <svg width="34" height="12" viewBox="0 0 34 12"><path d="M0 6h32M26 1l6 5-6 5" fill="none" stroke="#fff" stroke-width="1.5"/></svg>
</div>
<span class="dot" style="left:561px;top:808px;background:#fff"></span>
<span class="dot" style="left:584px;top:808px;border:1px solid #fff"></span>
<span class="dot" style="left:606px;top:808px;border:1px solid #fff"></span>
<span class="dot" style="left:631px;top:808px;border:1px solid #fff"></span>

<h2 class="abs heading styles-title">OFFER MULTIPLE EDITING STYLES</h2>
<p class="abs styles-sub">I will have 4 color editing styles (Colm's Hallmark, Bright &amp; Airy,<br>Silken Oak, Dreamy) and one black and white style</p>

<div class="tile grade-dreamy" style="left:72px;top:1229px;width:335px;height:220px" role="img" aria-label="Couple under a lit canopy at night in the dreamy edit: glowing amber light, deep violet shadows"><div class="frame"></div><div class="label">Dreamy</div></div>
<div class="tile grade-bw" style="left:72px;top:1459px;width:335px;height:220px" role="img" aria-label="Couple portrait in the black and white edit: neutral greys, strong contrast"><div class="frame"></div><div class="label">Black &amp; White</div></div>
<div class="tile grade-hallmark" style="left:417px;top:1229px;width:366px;height:450px" role="img" aria-label="Couple walking hand in hand by a waterfall in the signature edit: natural greens and true skin tones"><div class="frame" style="inset:22px 14px"></div><div class="label">Colm's Hallmark</div></div>
<div class="tile grade-airy" style="left:793px;top:1229px;width:335px;height:220px" role="img" aria-label="Couple on a garden path in the bright and airy edit: light pastel tones, soft contrast"><div class="frame"></div><div class="label">Bright &amp; Airy</div></div>
<div class="tile grade-oak" style="left:793px;top:1459px;width:335px;height:220px" role="img" aria-label="Couple in front of a brick building in the warm brown edit: rich rust and chocolate tones"><div class="frame"></div><div class="label">Silken Oak</div></div>

<h2 class="abs heading about-title">ABOUT ME</h2>
<div class="abs kicker" style="left:119px;top:1902px">WHO WE ARE</div>
<span class="line" style="left:263px;top:1913px;width:51px"></span>
<p class="abs about-text">I am an accountant by day, photographer by night. I once read a happy life is had by loving your job, loving your creative hobby and the love of family; photography is one part of that for me. I focus primarily on wedding photography in southern Ontario. I cover Toronto, Hamilton, Kitchener, Waterloo, London and anywhere in the world you want to send me. If you like what I do, please reach out; I'm happy to meet with you and chat more about your big day.</p>
<div class="btn-outline btn-ghost" style="left:125px;top:2170px;width:171px;height:43px">CONTACT ME
  <svg width="26" height="10" viewBox="0 0 26 10"><path d="M0 5h24M19 1l5 4-5 4" fill="none" stroke="#2b2b2b" stroke-width="1.4"/></svg>
</div>
<div class="photo" style="left:734px;top:1837px;width:322px;height:372px;background:linear-gradient(160deg,#9fb07f,#c9b9a2 50%,#6f8ab0)" role="img" aria-label="Photographer holding his baby daughter outdoors"></div>

<section class="abs portfolio-bg"></section>
<h2 class="abs heading portfolio-title">PORTFOLIO</h2>
<div class="abs kicker" style="left:64px;top:2495px">OUR RECENT WORK</div>
<div class="photo" style="left:70px;top:2715px;width:255px;height:357px;background:linear-gradient(180deg,#15203a,#3a3050 40%,#c86b3a 70%,#3a2a2a)" role="img" aria-label="Couple under a lit canopy at night"></div>
<div class="photo" style="left:341px;top:2548px;width:255px;height:358px;background:linear-gradient(180deg,#d98a2a,#e8b040 40%,#8f9a2a 75%,#6a7a20)" role="img" aria-label="Couple in a golden meadow at sunset"></div>
<div class="photo" style="left:341px;top:2924px;width:255px;height:358px;background:linear-gradient(150deg,#6a2a1e,#a5533a 40%,#e5ddd5 70%,#4a3a30)" role="img" aria-label="Couple embracing before autumn leaves"></div>
<div class="photo" style="left:610px;top:2423px;width:255px;height:359px;background:linear-gradient(160deg,#7a6a5a,#b54a3a 40%,#e6e0da 70%,#6a6058)" role="img" aria-label="Couple on stone steps by an old doorway"></div>
<div class="photo" style="left:610px;top:2799px;width:255px;height:358px;background:linear-gradient(180deg,#2f6fb5,#8fb8e0 45%,#3a76b0 75%,#2a4f78)" role="img" aria-label="Couple on a dock by the lake under a blue sky"></div>
<div class="photo" style="left:877px;top:2579px;width:257px;height:358px;background:linear-gradient(180deg,#e8a05a,#f4c27a 45%,#c8b040 70%,#8c9a30)" role="img" aria-label="Couple in a sunlit field at golden hour"></div>
<svg class="abs" style="left:799px;top:2525px" width="132" height="132" viewBox="0 0 132 132" aria-label="Contact me">
  <defs><path id="ring" d="M66 66m-44 0a44 44 0 1 1 88 0a44 44 0 1 1 -88 0"/></defs>
  <circle cx="66" cy="66" r="66" fill="#0a56a8"/>
  <text font-family="Raleway, sans-serif" font-size="11" fill="#fff" letter-spacing="2"><textPath href="#ring" startOffset="0">CONTACT ME</textPath></text>
  <text font-family="Raleway, sans-serif" font-size="11" fill="#fff" letter-spacing="2"><textPath href="#ring" startOffset="50%">CONTACT ME</textPath></text>
  <path d="M56 76L76 56M64 56h12v12" fill="none" stroke="#fff" stroke-width="1.8"/>
</svg>
<div class="btn-outline btn-ghost" style="left:929px;top:3193px;width:170px;height:44px">VIEW ALL
  <svg width="26" height="10" viewBox="0 0 26 10"><path d="M0 5h24M19 1l5 4-5 4" fill="none" stroke="#2b2b2b" stroke-width="1.4"/></svg>
</div>

<section class="abs serving"></section>
<div class="abs serving-frame"></div>
<h2 class="abs serving-title">ALSO SERVING</h2>
<p class="abs serving-cities">Toronto, London, Hamilton, Niagara, Cambridge,<br>Mississaug, Brampton, Burlington, Guelph</p>

<h2 class="abs heading test-title">TESTIMONIALS</h2>
<div class="abs kicker test-kicker">HAPPY CLIENTS</div>
<span class="line" style="left:484px;top:3899px;width:30px"></span>
<span class="line" style="left:687px;top:3899px;width:30px"></span>

<div class="arrow-btn" style="left:9px;top:4096px"><svg width="10" height="12" viewBox="0 0 10 12"><path d="M7 1L2 6l5 5" fill="none" stroke="#fff" stroke-width="1.6"/></svg></div>
<div class="arrow-btn" style="left:1153px;top:4096px"><svg width="10" height="12" viewBox="0 0 10 12"><path d="M3 1l5 5-5 5" fill="none" stroke="#fff" stroke-width="1.6"/></svg></div>

<article class="quote-card" style="left:68px">
  <div class="mark">”</div>
  <p>Colm is the absolute best! He did a SPECTACULAR job with our wedding photos. He got images of everything, even the things that we never thought he would notice. Hands down Colm is the best photographer I have seen in the area and you will not be disappointed.</p>
  <div class="who">NORA &amp; ELI</div>
</article>
<article class="quote-card" style="left:425px">
  <div class="mark">”</div>
  <p>Colm did an outstanding job on our wedding photos! We got so so much more for so so much less. Thanks again Colm, you exceeded our expectations and then some. I recommend him 100 times over!</p>
  <div class="who">SAM &amp; LENA</div>
</article>
<article class="quote-card" style="left:783px">
  <div class="mark">”</div>
  <p>Colm did a fabulous job on both our engagement and wedding photos. We were very impressed with not only the posed shots but also all off the candid ones. He was very professional, organized and accommodating. We have already recommended him to numerous people and will continue to do so!</p>
  <div class="who">OWEN &amp; TESS</div>
</article>
<div class="avatar" style="left:208px;top:4225px;background:linear-gradient(135deg,#c87a6a,#e8c0b0)" role="img" aria-label="Client couple portrait"></div>
<div class="avatar" style="left:566px;top:4225px;background:linear-gradient(135deg,#dfe0e6,#8a8fa0)" role="img" aria-label="Client couple portrait"></div>
<div class="avatar" style="left:923px;top:4225px;background:linear-gradient(135deg,#d99a4a,#8a6a40)" role="img" aria-label="Client couple portrait"></div>
<span class="dot" style="left:561px;top:4344px;background:#2b2b2b"></span>
<span class="dot" style="left:584px;top:4344px;border:1px solid #2b2b2b"></span>
<span class="dot" style="left:606px;top:4344px;border:1px solid #2b2b2b"></span>
<span class="dot" style="left:631px;top:4344px;border:1px solid #2b2b2b"></span>

<section class="abs contact-band"></section>
<div class="abs contact-panel"></div>
<div class="photo" style="left:99px;top:4496px;width:384px;height:440px;background:linear-gradient(150deg,#6a5a4a,#b54a32 40%,#e6e0da 70%,#5a5048)" role="img" aria-label="Couple on stone steps beside autumn leaves"></div>
<h2 class="abs heading contact-title">CONTACT US</h2>
<div class="abs kicker" style="left:548px;top:4594px">COLM V PHOTOGRAPHY</div>
<span class="line" style="left:794px;top:4605px;width:32px"></span>
<div class="field" style="left:553px;top:4661px;width:248px;height:53px">Name</div>
<div class="field" style="left:818px;top:4661px;width:248px;height:53px">Phone Number</div>
<div class="field" style="left:553px;top:4722px;width:513px;height:54px">Email Address</div>
<div class="field" style="left:553px;top:4784px;width:513px;height:92px">Event Date/ Info</div>
<div class="submit">CHECK AVAILABILITY</div>

<div class="abs footer-brand"><span class="name">Colm V</span><span class="tag">PHOTOGRAPHY</span></div>
<div class="info-icon" style="left:489px;top:5096px"><svg width="26" height="26" viewBox="0 0 24 24"><path d="M6.6 10.8a15 15 0 0 0 6.6 6.6l2.2-2.2a1 1 0 0 1 1-.25 11.4 11.4 0 0 0 3.6.57 1 1 0 0 1 1 1V20a1 1 0 0 1-1 1A17 17 0 0 1 3 4a1 1 0 0 1 1-1h3.5a1 1 0 0 1 1 1c0 1.25.2 2.45.57 3.57a1 1 0 0 1-.25 1z" fill="#fff"/></svg></div>
<div class="info" style="left:565px;top:5098px">CALL US<br>555-014-2290</div>
<div class="info-icon" style="left:785px;top:5096px"><svg width="26" height="20" viewBox="0 0 26 20"><rect x="1" y="1" width="24" height="18" rx="2" fill="#fff"/><path d="M2 3l11 8 11-8" fill="none" stroke="#0a56a8" stroke-width="1.6"/></svg></div>
<div class="info" style="left:863px;top:5098px">MAIL US<br>colm@colmvphotography.com</div>
<div class="abs rule"></div>
<div class="abs copy">Copyright © 2024 All Rights Reserved By Company name</div>
<span class="social" style="left:616px"></span>
<span class="social" style="left:653px"></span>
<div class="abs foot-links">HOME &nbsp;|&nbsp; THE TEAM &nbsp;|&nbsp; PORTFOLIO &nbsp;|&nbsp; BLOG &nbsp;|&nbsp; PRICING &nbsp;|&nbsp; CONTACT ME</div>

</body>
</html>
```